Granite, Brass and Shingle Roofing LLC needs a new business card

I need a new business card because I have a new address.
I do slate copper and tile roofs. My webpage is: www.granitebrassandshingleroofing.com

```html
<!DOCTYPE html>
<html lang="en">
<head>
<meta charset="utf-8">
<title>Granite, Brass &amp; Shingle Roofing – Business Card</title>
<link rel="stylesheet" href="https://fonts.googleapis.com/css2?family=Arimo:wght@400;700&display=swap">
<style>
  :root {
    --sky: #58b8e9;
    --sky-deep: #4eaee3;
    --ink: #0a0a0a;
    --band: #111111;
    --silver: #d9dbdd;
    --paper: #ffffff;
    --backdrop: #c9cccf;
    --icon: #58b8e9;
  }
  * { margin: 0; padding: 0; box-sizing: border-box; }
  html, body {
    width: 1187px; height: 1200px; overflow: hidden;
    background: var(--backdrop);
    font-family: "Arimo", Arial, sans-serif;
  }
  .canvas { position: relative; width: 1187px; height: 1200px; }

  .card {
    position: absolute; left: 207px; width: 773px; height: 439px; overflow: hidden;
  }
  .card--front { top: 117px; background: var(--sky); }
  .card--back { top: 642px; background: var(--band); }

  /* front */
  .front-sky {
    position: absolute; inset: 0 0 76px 0;
    background: linear-gradient(180deg, var(--sky) 0%, #5bbbe9 100%);
  }
  .front-rule {
    position: absolute; left: 0; right: 0; top: 363px; height: 6px;
    background: linear-gradient(90deg, #9fa3a6, var(--silver) 40%, #f4f4f4 60%, #a7aaad);
  }
  .front-band {
    position: absolute; left: 0; right: 0; bottom: 0; height: 70px;
    background: var(--band);
    display: flex; align-items: center; justify-content: center;
  }
  .front-url {
    color: var(--paper); font-size: 22px; font-weight: 700; letter-spacing: 1px;
    white-space: nowrap;
  }

  /* brand name lockup */
  .brand {
    position: absolute; display: flex; align-items: center; gap: 12px;
    color: var(--ink); font-weight: 700; line-height: 1.1;
  }
  .brand__mark { flex: none; background: var(--ink); }
  .brand--front { left: 150px; top: 190px; width: 480px; font-size: 30px; }
  .brand--front .brand__mark { width: 34px; height: 34px; }
  .brand--back { left: 36px; top: 160px; width: 340px; font-size: 23px; }
  .brand--back .brand__mark { width: 26px; height: 26px; }

  /* back */
  .back-sky {
    position: absolute; left: 0; top: 0; bottom: 0; width: 398px;
    background: linear-gradient(180deg, #5dbbe9 0%, var(--sky-deep) 100%);
  }
  .back-rule {
    position: absolute; left: 398px; top: 0; bottom: 0; width: 6px;
    background: linear-gradient(180deg, #b9bcbf, #eeeeee 50%, #a9acaf);
  }
  .contact {
    position: absolute; left: 430px; right: 8px; top: 92px; color: var(--paper);
    white-space: nowrap;
  }
  .contact__name { font-size: 31px; line-height: 1.05; }
  .contact__role { font-size: 25px; line-height: 1.1; margin-left: 2px; }
  .contact__address { margin-top: 30px; font-size: 17px; line-height: 27px; margin-left: 2px; }
  .contact__lines { margin-top: 18px; list-style: none; font-size: 17px; line-height: 26px; }
  .contact__lines li { display: flex; align-items: center; gap: 6px; }
  .contact__lines svg { width: 15px; height: 15px; flex: none; }
</style>
</head>
<body>
<main class="canvas">

  <section class="card card--front" aria-label="Card front">
    <div class="front-sky"></div>
    <div class="brand brand--front">
      <span class="brand__mark"></span>
      <span class="brand__name">Granite, Brass &amp; Shingle<br>Roofing</span>
    </div>
    <div class="front-rule"></div>
    <div class="front-band"><span class="front-url">www.granitebrassandshingleroofing.com</span></div>
  </section>

  <section class="card card--back" aria-label="Card back">
    <div class="back-sky"></div>
    <div class="brand brand--back">
      <span class="brand__mark"></span>
      <span class="brand__name">Granite, Brass &amp; Shingle<br>Roofing</span>
    </div>
    <div class="back-rule"></div>

    <div class="contact">
      <p class="contact__name">Lajos (Lou) Varga</p>
      <p class="contact__role">Owner</p>
      <p class="contact__address">2870 Millbrook Rd.<br>Millbrook, OH 44390</p>
      <ul class="contact__lines">
        <li>
          <svg viewBox="0 0 16 16" aria-hidden="true"><path fill="var(--icon)" d="M3.5 1.5l2.3 0 1 3.3-1.6 1.3c.8 1.8 2.2 3.2 4 4l1.3-1.6 3.3 1v2.3c0 .9-.7 1.5-1.6 1.5C6.8 13 3 9.2 2 3.1 2 2.2 2.6 1.5 3.5 1.5z"/></svg>
          <span>(440)555-0187</span>
        </li>
        <li>
          <svg viewBox="0 0 16 16" aria-hidden="true"><g fill="none" stroke="var(--icon)" stroke-width="1.4"><circle cx="8" cy="8" r="6.3"/><ellipse cx="8" cy="8" rx="2.8" ry="6.3"/><path d="M1.7 8h12.6M2.6 5h10.8M2.6 11h10.8"/></g></svg>
          <span>www.granitebrassandshingleroofing.com</span>
        </li>
        <li>
          <svg viewBox="0 0 16 16" aria-hidden="true"><rect x="1" y="3.5" width="14" height="9" fill="var(--icon)"/><path d="M1 3.5l7 5 7-5" fill="none" stroke="var(--band)" stroke-width="1.2"/></svg>
          <span>gbsroofingllc@mail.com</span>
        </li>
      </ul>
    </div>
  </section>

</main>
</body>
</html>
```